Vitamin design-two ranges zephLUMA and kessarineLUMA

Need attractive unique packaging for a range of multivitamins and minerals starting with zephLUMA which aids cognitive function. Also there is a product we also want to produce which is called kessarineluma so we would like the design to be readily adjusted to fit this product also. KessarineLUMA design should reflect natural, fruit and vegetable content . We would like two variants on same basic design. One to reflect Zephluma and one to fit Kessarineluma. The brand is
Corvantaluma and the word luma should be prominent in the design.

Target Market(s)

US market

Industry/Entity Type

Vitamin

Requirements
Must have
• Company will send me template that design needs to fit into and packaging needs to have room for product ingredients and details. Also the brand must be transferable. We are looking to create a range of vitamins around the name corvantaluma. This is the first in a range so we would like the word "luma" in zephluma to be prominent.
Nice to have
• Something bright and appealing, eye catching and unique. Transferable design that fits both products and transferable to some others
• I'll email specifications from company around size of labels and regulations but here are some basics
• ZephLUMA capsules - label size 2.5 x6 for both 30 and 60 count.Bottle
• 30ct 100cc / 60ct 120cc
• Kessarine LUMA Label size 3x8 for 90ct bottle 300c
Should not have
• No claims of 100% natural or definitive claims

```html
<!DOCTYPE html>
<html lang="en">
<head>
<meta charset="utf-8">
<title>zephLUMA Multivit Complete Label</title>
<link rel="stylesheet" href="https://fonts.googleapis.com/css2?family=Bitter:wght@500;600;700;800&display=swap">
<style>
  :root {
    --backdrop-deep: #7a4a1c;
    --backdrop-glow: #b0722c;
    --teal-dark: #0b3540;
    --teal-mid: #3f6a72;
    --teal-light: #547e85;
    --gold-dark: #b98a2a;
    --gold-light: #f5dd98;
    --gold-text: #f0d48a;
    --cream: #f6e6b4;
    --ink-dark: #3a2a12;
    --pill-green: #b3d27a;
    --pill-text: #2f4a12;
    --swoosh-green: #9bd13c;
    --white: #ffffff;
  }
  * { box-sizing: border-box; margin: 0; padding: 0; }
  html, body { width: 1200px; height: 900px; overflow: hidden; }
  body {
    background: radial-gradient(ellipse at center, var(--backdrop-glow) 0%, var(--backdrop-deep) 75%);
    font-family: "Bitter", Georgia, serif;
  }
  .label {
    position: absolute;
    left: 300px; top: 120px;
    width: 600px; height: 660px;
    background: linear-gradient(90deg, var(--teal-dark) 0%, var(--teal-mid) 30%, var(--teal-light) 55%, var(--teal-mid) 75%, var(--teal-dark) 100%);
    text-align: center;
    color: var(--white);
    overflow: hidden;
  }
  .gold-band {
    position: absolute; left: 0; width: 100%; height: 18px;
    background: linear-gradient(180deg, var(--gold-light), var(--gold-dark));
  }
  .gold-band.top { top: 0; }
  .gold-band.bottom { bottom: 0; height: 22px; }
  .brand-mark {
    position: absolute; left: 50%; top: 48px;
    width: 88px; height: 88px; margin-left: -44px;
    border-radius: 50%;
    background: var(--cream);
    border: 4px solid var(--gold-dark);
  }
  .brand-lockup { position: absolute; top: 150px; width: 100%; color: var(--gold-text); font-weight: 600; }
  .product-line { font-size: 50px; letter-spacing: 1px; line-height: 1.1; }
  .powered-by { font-size: 14px; line-height: 1.2; }
  .company-name { font-size: 20px; letter-spacing: 1px; }
  .claim-pill {
    position: absolute; top: 268px; left: 50%; transform: translateX(-50%);
    background: var(--pill-green); color: var(--pill-text);
    font-size: 15px; font-weight: 700; padding: 3px 12px; border-radius: 4px;
  }
  .product-name { position: absolute; top: 300px; width: 100%; }
  .product-name .main { font-size: 70px; font-weight: 800; letter-spacing: 1px; line-height: 1; }
  .product-name .sub { font-size: 42px; font-weight: 500; line-height: 1.1; }
  .swoosh { position: absolute; left: 0; top: 410px; width: 600px; height: 60px; }
  .details {
    position: absolute; top: 480px; left: 40px; right: 40px;
    display: flex; text-align: left; font-size: 18px; font-weight: 700; line-height: 1.25;
  }
  .details p { flex: 1; padding: 4px 14px; }
  .details p + p { border-left: 2px solid rgba(255,255,255,0.7); }
  .count-tab {
    position: absolute; bottom: 0; left: 50%; width: 220px; height: 72px; margin-left: -110px;
    background: linear-gradient(180deg, var(--gold-light), #e9c774);
    border-radius: 110px 110px 0 0 / 40px 40px 0 0;
    color: var(--ink-dark); font-weight: 700; font-size: 20px; line-height: 1.1;
    padding-top: 14px;
  }
</style>
</head>
<body>
  <main class="label">
    <div class="gold-band top"></div>
    <div class="brand-mark"></div>
    <div class="brand-lockup">
      <div class="product-line">zephLUMA</div>
      <div class="powered-by">powered by</div>
      <div class="company-name">CORVANTALUMA</div>
    </div>
    <div class="claim-pill">100% GLUTEN FREE</div>
    <div class="product-name">
      <div class="main">MULTIVIT</div>
      <div class="sub">Complete</div>
    </div>
    <svg class="swoosh" viewBox="0 0 600 60" aria-hidden="true">
      <path d="M0 30 C150 10 250 55 380 42 C470 34 540 20 600 14 L600 22 C540 30 470 44 380 50 C250 60 150 22 0 38 Z" fill="var(--swoosh-green)" opacity="0.85"/>
    </svg>
    <div class="details">
      <p>Dietary Supplement<br>to LUMA Brain</p>
      <p>25 Key Nutrients for<br>Daily Nutritional<br>Support</p>
    </div>
    <div class="gold-band bottom"></div>
    <div class="count-tab">120<br>Capsules</div>
  </main>
</body>
</html>
```